" Empresa que trabalha com danças urbanas. Workhops, Batalhas, Performances, Palestras, Bate-papos, Jam Sessions. Também possui um projeto social em comunidades. "

```html
<!DOCTYPE html>
<html lang="pt-BR">
<head>
<meta charset="utf-8">
<title>Passo Livre – Inscrição Online</title>
<link href="https://fonts.googleapis.com/css2?family=Open+Sans:wght@400;600;700&family=Oswald:wght@500;700&display=swap" rel="stylesheet">
<style>
:root{
  --outer:#3a3a3a;
  --page:#262626;
  --page-line:#2d2d2d;
  --panel:#343434;
  --field:#4a4a4a;
  --field-text:#8a8a8a;
  --label:#d8d8d8;
  --white:#ffffff;
  --silver-1:#f2f2f2;
  --silver-2:#b8b8b8;
  --silver-3:#8c8c8c;
  --green:#7db51e;
  --yellow:#e3d21a;
  --dark:#151515;
  --muted:#9a9a9a;
}
*{box-sizing:border-box;margin:0;padding:0}
html,body{width:1200px;height:1200px;overflow:hidden}
body{background:var(--outer);font-family:"Open Sans",Arial,sans-serif;color:var(--label);position:relative}
.abs{position:absolute}

/* header */
.top-line{left:0;top:0;width:1200px;height:7px;background:linear-gradient(90deg,var(--green),var(--yellow),var(--green))}
.header{left:0;top:7px;width:1200px;height:95px;background:linear-gradient(180deg,#cfcfcf 0%,#9d9d9d 55%,#6f6f6f 100%)}
.header::after{content:"";position:absolute;left:0;right:0;bottom:0;height:40px;background:linear-gradient(180deg,#2c2c2c,#1a1a1a)}
.signup-box{left:516px;top:14px;width:168px;height:78px;background:linear-gradient(180deg,#ffffff,#d9d9d9);border:2px solid #777;z-index:2;text-align:center;padding-top:8px}
.signup-box p{font-size:11px;line-height:14px;color:#333}
.signup-box strong{color:#111}
.signup-box .btn{display:inline-block;margin-top:6px;font-size:8px;font-weight:700;background:#333;color:#fff;padding:3px 10px}
.social-top{left:722px;top:40px;display:flex;gap:5px;z-index:2}
.social-top span{width:16px;height:16px;background:#333;border:1px solid #666}
.social-top .like{width:40px;background:#e8e8e8;border-color:#999}
.dancer{left:1034px;top:20px;width:70px;height:82px;background:linear-gradient(180deg,#222,#111);border-radius:30px 30px 6px 6px;z-index:2}

/* nav */
.nav{left:312px;top:106px;width:576px;height:36px;background:linear-gradient(180deg,var(--silver-1),var(--silver-2) 60%,var(--silver-3));display:flex;justify-content:space-between;align-items:center;padding:0 14px}
.nav a{font-size:10.5px;font-weight:600;color:#333;text-decoration:none;text-transform:uppercase}
.nav a.active{color:#000;font-weight:700}
.nav-side{top:106px;height:36px;width:221px;background:linear-gradient(180deg,#9b9b9b,#6b6b6b)}
.subbar{left:91px;top:142px;width:1018px;height:26px;background:#1b1b1b;border-bottom:3px solid var(--green);padding-left:221px;display:flex;gap:26px;align-items:center;font-size:10px}
.subbar b{color:var(--yellow);font-weight:700}
.subbar span{color:var(--green)}

/* page */
.page{left:91px;top:168px;width:1018px;height:840px;background:repeating-linear-gradient(180deg,var(--page) 0,var(--page) 2px,var(--page-line) 2px,var(--page-line) 3px)}
.brand{left:300px;top:204px;width:204px;height:144px;background:linear-gradient(180deg,#dcdcdc,#8e8e8e);border:3px solid #e8e8e8;display:flex;align-items:center;justify-content:center}
.brand span{font-family:"Oswald",sans-serif;font-weight:700;font-size:34px;color:#1d1d1d}
.intro{left:512px;top:230px;font-size:13px;color:var(--label)}
.intro b{color:var(--white)}
.download{top:284px;display:flex;gap:8px;align-items:center;font-size:10px;line-height:13px;color:var(--label)}
.download b{color:var(--white);font-weight:700}
.download svg{flex:none}

.banner{left:372px;top:391px;width:456px;height:53px;background:linear-gradient(180deg,#f4f4f4,#a9a9a9);clip-path:polygon(3% 0,100% 0,97% 100%,0 100%);display:flex;align-items:center;justify-content:center}
.banner span{background:#1e1e1e;color:var(--white);font-family:"Oswald",sans-serif;font-weight:700;font-size:22px;padding:6px 46px;letter-spacing:.5px}

/* form */
.form{left:384px;top:456px;width:444px;height:528px;background:var(--panel);border-radius:6px;padding:16px 20px}
.form-head{display:flex;justify-content:space-between;align-items:center;font-size:12px;color:var(--white);border-bottom:1px solid #555;padding-bottom:6px}
.checks{display:flex;gap:16px;font-size:8px;font-weight:700;color:var(--white);text-transform:uppercase;align-items:center}
.checks i{display:inline-block;width:9px;height:9px;background:#fff;margin-right:4px;vertical-align:middle}
.cats{justify-content:center;margin:10px 0 8px}
.row{display:flex;gap:10px;margin-top:6px}
.f{display:flex;flex-direction:column}
.f label{font-size:9px;font-weight:700;color:var(--label);margin-bottom:3px}
.f span{height:17px;background:var(--field);font-size:8px;color:var(--field-text);padding:3px 5px;white-space:nowrap;overflow:hidden}
.w3{width:128px}.w2{width:180px}.w4{width:230px}.wfull{width:390px}
.f .area{height:72px}
.actions{display:flex;gap:16px;margin-top:22px;padding-left:4px}
.actions span{background:#222;color:var(--white);font-size:9px;font-weight:700;padding:6px 12px}

/* footer */
.foot-band{left:91px;top:1008px;width:1018px;height:30px;background:linear-gradient(180deg,#ededed,#9a9a9a);display:flex;justify-content:center;align-items:center;gap:6px}
.foot-band span{width:14px;height:14px;background:#333}
.foot-dark{left:91px;top:1038px;width:1018px;height:162px;background:#1a1a1a}
.follow{left:91px;top:1046px;width:1018px;text-align:center;font-size:10px;color:var(--label)}
.widget{left:511px;top:1063px;width:178px;height:106px;background:#f4f4f4;padding:6px}
.widget .wtop{display:flex;gap:6px;align-items:center;font-size:8px;color:#333}
.widget .wtop i{width:22px;height:22px;background:#555}
.thumbs{display:grid;grid-template-columns:repeat(5,1fr);gap:3px;margin-top:6px}
.thumbs span{height:28px;background:linear-gradient(135deg,#b59a86,#6f5a4e)}
.copy{left:91px;top:1178px;width:1018px;text-align:center;font-size:8px;color:var(--muted)}
</style>
</head>
<body>
<div class="abs top-line"></div>
<div class="abs header"></div>
<div class="abs signup-box"><p>Saiba de tudo que<br>rola na <strong>Passo Livre</strong></p><span class="btn">CADASTRE-SE</span></div>
<div class="abs social-top"><span class="like"></span><span></span><span></span><span></span><span></span></div>
<div class="abs dancer" role="img" aria-label="Silhueta de dançarino de street dance"></div>

<div class="abs nav-side" style="left:91px"></div>
<div class="abs nav-side" style="left:888px"></div>
<nav class="abs nav">
  <a>Home</a><a class="active">Sobre</a><a>Eventos</a><a>Projeto Social</a><a>Parceiros</a><a>Coreografia</a><a>Equipe</a><a>Shop</a><a>News</a><a>Contato</a>
</nav>
<div class="abs subbar"><b>Apresentação:</b><span>Festival 2015</span><span>Festival 2016</span><span>Festival 2017</span></div>

<div class="abs page"></div>
<div class="abs brand"><span>Passo Livre</span></div>
<p class="abs intro">Faça sua <b>inscrição</b> abaixo, ou faça o <b>download</b> do arquivo e nos envie!</p>
<div class="abs download" style="left:530px">
  <svg width="18" height="22" viewBox="0 0 18 22"><rect x="1" y="1" width="16" height="20" fill="none" stroke="#ddd" stroke-width="2"/><line x1="5" y1="8" x2="13" y2="8" stroke="#ddd" stroke-width="2"/><line x1="5" y1="13" x2="13" y2="13" stroke="#ddd" stroke-width="2"/></svg>
  <p>FICHA DE INSCRIÇÃO<br><b>INDIVIDUAL</b></p>
</div>
<div class="abs download" style="left:700px">
  <svg width="18" height="22" viewBox="0 0 18 22"><rect x="1" y="1" width="16" height="20" fill="none" stroke="#ddd" stroke-width="2"/><line x1="5" y1="8" x2="13" y2="8" stroke="#ddd" stroke-width="2"/><line x1="5" y1="13" x2="13" y2="13" stroke="#ddd" stroke-width="2"/></svg>
  <p>FICHA DE INSCRIÇÃO<br><b>GRUPO</b></p>
</div>

<div class="abs banner"><span>INSCRIÇÃO ONLINE</span></div>

<form class="abs form">
  <div class="form-head"><span>Informe seus dados</span><div class="checks"><span><i></i>Individual</span><span><i></i>Grupo</span></div></div>
  <div class="checks cats"><span><i></i>Passiste simples</span><span><i></i>Passiste dinâmico</span><span><i></i>Aberta avulsa</span></div>
  <div class="row"><div class="f w2"><label>Nome</label><span>Informe seu nome</span></div><div class="f w2"><label>Sobrenome</label><span>Informe seu sobrenome</span></div></div>
  <div class="row"><div class="f w4"><label>Nome Artístico</label><span>Informe o nome artístico</span></div></div>
  <div class="row"><div class="f w4"><label>Data de Nascimento</label><span>Informe a data de nascimento</span></div></div>
  <div class="row"><div class="f w3"><label>Endereço</label><span>Informe seu endereço</span></div><div class="f w3"><label>Complemento</label><span>Informe o complemento</span></div><div class="f w3"><label>Bairro</label><span>Informe o bairro</span></div></div>
  <div class="row"><div class="f w3"><label>Cidade</label><span>Informe a cidade</span></div><div class="f w3"><label>Estado (UF)</label><span>Informe seu estado</span></div><div class="f w3"><label>CEP</label><span>Informe seu CEP</span></div></div>
  <div class="row"><div class="f w2"><label>RG</label><span>Informe seu RG</span></div><div class="f w2"><label>CPF</label><span>Informe seu CPF</span></div></div>
  <div class="row"><div class="f w2"><label>E-mail</label><span>Informe seu e-mail</span></div></div>
  <div class="row"><div class="f w3"><label>Telefone Fixo</label><span>(00) 0000-0000</span></div><div class="f w3"><label>Telefone Celular</label><span>(00) 0000-0000</span></div><div class="f w3"><label>Telefone Opcional</label><span>(00) 0000-0000</span></div></div>
  <div class="row"><div class="f wfull"><label>Observação</label><span class="area">Deixe aqui informações adicionais ou observações</span></div></div>
  <div class="actions"><span>ENVIAR</span><span>ANEXAR ARQUIVOS</span></div>
</form>

<div class="abs foot-band"><span></span><span></span><span></span><span></span></div>
<div class="abs foot-dark"></div>
<p class="abs follow">Acompanhe a Passo Livre nas redes sociais</p>
<div class="abs widget">
  <div class="wtop"><i></i><span><b>Passo Livre</b><br>1.200 curtidas</span></div>
  <div class="thumbs" role="img" aria-label="Fotos de perfil de seguidores">
    <span></span><span></span><span></span><span></span><span></span>
    <span></span><span></span><span></span><span></span><span></span>
  </div>
</div>
<p class="abs copy">Copyright © 2017 Passo Livre. Todos os direitos reservados.</p>
</body>
</html>
```